E-commerce portal dedicated for selling books

We are looking for a design of a professional and official e-commerce web-site for a new company that is specialized in selling books (both books formats, printed and electronic), we’ll deal also with used-books where we plan to buy used books and re-sell them to other clients, or let the clients can sell their used-books directly to another client,
Web site must be very clear for users who like to brows the site contents or to buy a book, we will make the books available in discounted prices.
Customer should be able to perform the following actions in the site:
Search the book he/she is looking for easily
Get a brief description and details about the author, publisher, book content, browse the book’s content, browse first 20 pages ,
View similar or related books and a list of books that other users who bought this books also bought
Read and write reviews
Sign-up in the site
Complete the purchase process
Users can also sell or buy used-books from the site.
Look and feel:
The site’s look and feel is preferred to be clean, simple and balanced
Web site design is preferred to be simple with no strong or dark colors
User should feel comfort when looking at the home page because the design simplicity and comfortable colors
I liked the following sites’ look and feel:
http://www.lumirat.ae/
http://www.zelvik.com/
http://www.quillandfernbooks.com/
Please be sure to include all common elements that are used in the e-commerce web sites like Search, online form(s), shopping cart / ordering, user log in/member, printer-friendly function, subscription to newsletter.....
Industry/Entity Type
E-Commerce
Look and feel

```html
<!DOCTYPE html>
<html lang="en">
<head>
<meta charset="utf-8">
<title>Leafmark – The Biggest Choice on the Web</title>
<link href="https://fonts.googleapis.com/css2?family=Open+Sans:wght@300;400;600&display=swap" rel="stylesheet">
<style>
:root{
  --brown:#3e3632;
  --brown-light:#5a4f49;
  --green:#8cc63f;
  --green-text:#8cc63f;
  --text:#444;
  --price:#cc1f1f;
}
*{box-sizing:border-box;margin:0;padding:0}
html,body{width:805px;height:1200px;overflow:hidden}
body{position:relative;background:#fff;font-family:'Open Sans',Arial,sans-serif;color:var(--text)}
.abs{position:absolute}

/* top bar */
.topbar{left:0;top:0;width:805px;height:54px;background:linear-gradient(#f4f4f4,#e9e9e9);border-bottom:1px solid #ddd}
.search{left:88px;top:16px;width:344px;height:24px;background:#fff;border:1px solid #d5d5d5;display:flex;align-items:center;font-size:8px;color:#aaa;font-style:italic}
.search .query{flex:1;padding-left:8px}
.search .scope{width:104px;border-left:1px solid #ddd;padding-left:12px;font-style:normal}
.search-btn{left:434px;top:15px;width:63px;height:26px;background:var(--brown);color:#fff;font-size:10px;display:flex;align-items:center;justify-content:center}
.account{left:529px;top:24px;font-size:7.5px;color:#444;display:flex;gap:8px;align-items:center}
.account .sep{color:#bbb}

/* brand */
.brand{left:88px;top:60px;font-size:30px;font-weight:400;letter-spacing:0.5px;line-height:34px;color:#333}
.tagline{left:89px;top:90px;font-size:9.5px;color:#bbb;letter-spacing:0.3px}

/* green band */
.band{left:0;top:122px;width:805px;height:318px;background:linear-gradient(#a5d760,#c3e691 55%,#b1dd74)}

/* nav */
.nav{left:88px;top:110px;width:629px;height:26px;background:var(--brown);display:flex;align-items:center;padding-left:12px;gap:27px;font-size:9px;color:#fff;box-shadow:0 4px 6px rgba(0,0,0,.15)}

/* slider */
.slider{left:88px;top:157px;width:629px;height:224px;border:2px solid var(--brown-light);background:linear-gradient(#fff,#ececec)}
.cover{left:61px;top:13px;width:157px;height:194px;background:linear-gradient(135deg,#9ccf3a 0%,#d9c7a8 40%,#c9a77f 70%,#b3c7d8 100%)}
.slide-title{left:235px;top:43px;font-size:25px;font-weight:400;color:#444;letter-spacing:0.3px;white-space:nowrap}
.slide-sub{left:236px;top:74px;font-size:13px;color:#777}
.slide-rule{left:236px;top:102px;width:323px;height:1px;background:#b9d98c}
.slide-text{left:236px;top:112px;width:325px;font-size:8px;line-height:10px;color:#666}
.shop-btn{left:236px;top:156px;width:66px;height:22px;background:var(--brown-light);color:#fff;font-size:8.5px;display:flex;align-items:center;justify-content:center}
.arrow{width:17px;height:17px;border-radius:50%;background:#e3e3e3;top:103px}
.pager{left:560px;top:202px;display:flex;gap:3px}
.pager b{width:9px;height:9px;font-size:6px;color:#333;background:var(--green);display:flex;align-items:center;justify-content:center;font-weight:400}
.pager b.on{background:#333;color:#fff}

/* welcome */
.welcome{left:88px;top:402px;width:629px;height:86px;background:linear-gradient(#f7f7f7,#e9e9e9);border:1px solid #ccc}
.welcome h1{position:absolute;left:10px;top:5px;font-size:24px;font-weight:400;color:#333;letter-spacing:0.5px}
.welcome h1 span{color:var(--green-text)}
.welcome .rule{position:absolute;left:325px;top:28px;width:287px;height:1px;background:#a9d36a}
.dot{width:5px;height:5px;border-radius:50%;background:#a9d36a}
.welcome p{position:absolute;left:10px;top:42px;width:610px;font-size:7.5px;line-height:11.3px;color:#666}

/* categories */
.categories{left:88px;top:506px;width:165px;height:530px;border:1px solid #ccc;border-top:none}
.categories h2{height:25px;background:var(--brown);color:#fff;font-size:12.5px;font-weight:400;padding:4px 0 0 8px}
.categories ul{list-style:none;padding:2px 6px 0}
.categories li{height:19.5px;line-height:19px;font-size:7.5px;color:#555;border-bottom:1px solid #e1e1e1;padding-left:2px}

/* featured */
.featured-title{left:269px;top:507px;font-size:13px;color:#333;font-weight:400}
.featured-rule{left:388px;top:518px;width:324px;height:1px;background:#a9d36a}
.grid{left:270px;top:534px;display:grid;grid-template-columns:248px 248px;grid-auto-rows:128px}
.book{position:relative}
.thumb{position:absolute;left:0;top:0;width:102px;height:110px;border:1px solid #ccc;background:#fff;padding:9px 10px}
.thumb div{width:100%;height:100%}
.art-voices{background:linear-gradient(#ecece2 0 30%,#6f8a4a 30%,#9b2f2a 60%,#3e6033 100%)}
.art-dusk{background:linear-gradient(160deg,#1b1b1b,#4a4a4a 50%,#0e0e0e)}
.art-dusk2{background:linear-gradient(#1a2430,#3a4450 50%,#141a22)}
.art-psych{background:linear-gradient(#c1121d 0 55%,#e6e6ef 60%,#2a40a0 66%,#1e2f7a)}
.art-portrait{background:linear-gradient(#fafafa 0 15%,#bdbdbd 50%,#2c2c2c)}
.info{position:absolute;left:108px;top:0;width:135px}
.info h3{font-size:7.5px;font-weight:400;color:#333;line-height:9px;height:18px;text-transform:uppercase}
.info .author{font-size:6.5px;color:#999;margin-top:3px}
.info .price{font-size:11px;color:var(--price);margin-top:4px}
.stars{display:flex;gap:1px;margin-top:8px;height:12px}
.stars svg{width:12px;height:12px}
.btn-view{margin-top:8px;width:52px;height:15px;background:var(--green);color:#fff;font-size:6.5px;display:flex;align-items:center;justify-content:center}
.btn-cart{margin-top:7px;width:52px;height:15px;background:var(--brown-light);color:#fff;font-size:6.5px;display:flex;align-items:center;justify-content:center}

/* promo + newsletter */
.promo{left:88px;top:1058px;width:425px;height:97px;border:2px solid #ccc;background:linear-gradient(90deg,#fff,#f1f1f1)}
.promo-art{left:0;top:0;width:80px;height:93px;background:linear-gradient(150deg,#3a4148,#7c8a86 45%,#c7cfca)}
.promo-line1{left:102px;top:12px;font-size:34px;color:#444;line-height:36px;white-space:nowrap}
.promo-line1 span{font-size:23px;color:var(--green-text)}
.promo-line1 em{font-style:normal;font-size:23px;color:#444}
.promo-rule{left:102px;top:53px;width:282px;height:1px;background:#ccc}
.promo-line2{left:102px;top:55px;font-size:29px;color:var(--green-text);line-height:34px;white-space:nowrap}
.promo-line2 span{color:#444;font-size:25px}
.divider{left:532px;top:1064px;width:1px;height:84px;background:#ddd}
.news-title{left:553px;top:1059px;width:164px;height:26px;background:var(--brown);color:#fff;font-size:12px;padding:4px 0 0 8px}
.news-input{left:561px;top:1102px;width:156px;height:20px;border:1px solid #d3d3d3;font-size:7px;color:#aaa;padding:5px 0 0 4px}
.news-btn{left:641px;top:1132px;width:76px;height:23px;background:var(--brown-light);color:#fff;font-size:8.5px;display:flex;align-items:center;justify-content:center}

/* footer */
.footer{left:88px;top:1166px;width:629px;height:34px;background:var(--brown);display:flex;align-items:center;padding:0 10px;color:#fff;font-size:7.5px}
.footer nav{display:flex;gap:6px;align-items:center}
.footer .sep{color:#7a706a}
.footer .copy{margin-left:auto;font-size:6px}
</style>
</head>
<body>
<svg width="0" height="0" class="abs" aria-hidden="true">
  <defs>
    <symbol id="star" viewBox="0 0 24 24"><path d="M12 1.5l3.2 6.9 7.3.8-5.4 5 1.5 7.3L12 17.8l-6.6 3.7 1.5-7.3-5.4-5 7.3-.8z" fill="#f4c400" stroke="#b58d00" stroke-width="1.2"/></symbol>
  </defs>
</svg>

<header>
  <div class="abs topbar"></div>
  <div class="abs search"><span class="query">Search Your Books here....</span><span class="scope">All Books</span></div>
  <div class="abs search-btn">SEARCH</div>
  <div class="abs account">
    <span>SIGN IN</span><span class="sep">|</span>
    <span><svg width="9" height="8" viewBox="0 0 12 10"><path d="M0 1h2l2 6h6l1.5-4.5H3" fill="none" stroke="#444" stroke-width="1"/><circle cx="5" cy="9" r="0.9" fill="#444"/><circle cx="9" cy="9" r="0.9" fill="#444"/></svg> SHOPPING CART</span><span class="sep">|</span>
    <span>WISHLIST ▾</span>
  </div>
  <div class="abs brand">LEAFMARK</div>
  <div class="abs tagline">THE BIGGEST CHOICE ON THE WEB</div>
</header>

<div class="abs band"></div>
<nav class="abs nav">
  <span>HOME</span><span>ABOUT US</span><span>BOOKS</span><span>SERVICES</span><span>ALL BOOKS</span><span>REVIEWS</span><span>CONTACT US</span><span>FAQS</span>
</nav>

<section class="abs slider">
  <div class="abs arrow" style="left:17px"></div>
  <div class="abs arrow" style="left:592px"></div>
  <div class="abs cover" role="img" aria-label="Magazine cover with a mother hugging her daughter"></div>
  <div class="abs slide-title">FAMILY HOURS MAGAZINE</div>
  <div class="abs slide-sub">by Halden Press Group</div>
  <div class="abs slide-rule"></div>
  <p class="abs slide-text">Lorem ipsum dolor sit amet conse ctetur adipisicing elit, sed do eiusmod tempor incididunt ut labore et dolore magna aliqua. Ut enim ad minim veniam, quis nostrud exercitation ullamco</p>
  <div class="abs shop-btn">SHOP NOW</div>
  <div class="abs pager"><b class="on">1</b><b>2</b><b>3</b><b>4</b><b>5</b></div>
</section>

<section class="abs welcome">
  <h1>WELCOME TO <span>LEAFMARK!</span></h1>
  <div class="rule"></div>
  <div class="abs dot" style="left:610px;top:26px"></div>
  <p>Lorem ipsum dolor sit amet conse ctetur adipisicing elit, sed do eiusmod tempor incididunt ut labore et dolore magna aliqua. Ut enim ad minim veniam, quis nostrud exercitation ullamco.Lorem ipsum dolor sit amet conse ctetur adipisicing elit, sed do eiusmod tempor incididunt ut labore et dolore magna aliqua. Ut enim ad minim veniam, quis nostrud exercitation ullamco.</p>
</section>

<aside class="abs categories">
  <h2>CATAGORIES</h2>
  <ul>
    <li>E-Books</li><li>Biography Books</li><li>Romance Books</li><li>Health &amp; Fitness Books</li><li>Children Books</li><li>Business &amp; investing Books</li><li>Art &amp; Photography Books</li><li>Computer Books</li><li>Entertainment Books</li><li>Pschology Books</li><li>Religion Books</li><li>Romance Books</li><li>History Books</li><li>Mystery Books</li><li>Finance Books</li><li>Politics Books</li><li>Cooking Books</li><li>Science Books</li><li>E-Books</li><li>Biography Books</li><li>Romance Books</li><li>Health &amp; Fitness Books</li><li>Children Books</li><li>Business &amp; investing Books</li><li>Art &amp; Photography Books</li>
  </ul>
</aside>

<h2 class="abs featured-title">FEATURED BOOKS</h2>
<div class="abs featured-rule"></div>
<div class="abs dot" style="left:713px;top:516px"></div>

<section class="abs grid">
  <article class="book">
    <div class="thumb"><div class="art-voices" role="img" aria-label="Book cover with a red carpet"></div></div>
    <div class="info"><h3>Famous Voices<br>in Print</h3><div class="author">Arthur: Warren Vessel</div><div class="price">Price: $ 22</div>
      <div class="stars"><svg><use href="#star"/></svg><svg><use href="#star"/></svg><svg><use href="#star"/></svg><svg><use href="#star"/></svg><svg><use href="#star"/></svg></div>
      <div class="btn-view">View Book</div><div class="btn-cart">Add to Cart</div></div>
  </article>
  <article class="book">
    <div class="thumb"><div class="art-dusk" role="img" aria-label="Dark book cover with a portrait"></div></div>
    <div class="info"><h3>Dusk Chronicle<br>(Umbra)</h3><div class="author">Arthur: Stella Marlow</div><div class="price">Price: $ 30</div>
      <div class="stars"><svg><use href="#star"/></svg><svg><use href="#star"/></svg><svg><use href="#star"/></svg><svg><use href="#star"/></svg></div>
      <div class="btn-view">View Book</div><div class="btn-cart">Add to Cart</div></div>
  </article>
  <article class="book">
    <div class="thumb"><div class="art-dusk2" role="img" aria-label="Dark book cover with three figures"></div></div>
    <div class="info"><h3>Dusk Chronicle<br>(Umbra)</h3><div class="author">Arthur: Stella Marlow</div><div class="price">Price: $ 20</div>
      <div class="stars"><svg><use href="#star"/></svg><svg><use href="#star"/></svg><svg><use href="#star"/></svg><svg><use href="#star"/></svg><svg><use href="#star"/></svg></div>
      <div class="btn-view">View Book</div><div class="btn-cart">Add to Cart</div></div>
  </article>
  <article class="book">
    <div class="thumb"><div class="art-psych" role="img" aria-label="Red and blue book cover"></div></div>
    <div class="info"><h3>Psychology<br>&nbsp;</h3><div class="author">Arthur: Glen Butterfield</div><div class="price">Price: $ 15</div>
      <div class="stars"><svg><use href="#star"/></svg><svg><use href="#star"/></svg><svg><use href="#star"/></svg><svg><use href="#star"/></svg></div>
      <div class="btn-view">View Book</div><div class="btn-cart">Add to Cart</div></div>
  </article>
  <article class="book">
    <div class="thumb"><div class="art-voices" role="img" aria-label="Book cover with a red carpet"></div></div>
    <div class="info"><h3>Famous Voices<br>in Print</h3><div class="author">Arthur: Warren Vessel</div><div class="price">Price: $ 27</div>
      <div class="stars"><svg><use href="#star"/></svg><svg><use href="#star"/></svg><svg><use href="#star"/></svg><svg><use href="#star"/></svg></div>
      <div class="btn-view">View Book</div><div class="btn-cart">Add to Cart</div></div>
  </article>
  <article class="book">
    <div class="thumb"><div class="art-portrait" role="img" aria-label="Black and white biography cover portrait"></div></div>
    <div class="info"><h3>The Inventor<br>&nbsp;</h3><div class="author">Arthur: Walden Isaacs</div><div class="price">Price: $ 35</div>
      <div class="stars"><svg><use href="#star"/></svg><svg><use href="#star"/></svg><svg><use href="#star"/></svg><svg><use href="#star"/></svg><svg><use href="#star"/></svg></div>
      <div class="btn-view">View Book</div><div class="btn-cart">Add to Cart</div></div>
  </article>
  <article class="book">
    <div class="thumb"><div class="art-voices" role="img" aria-label="Book cover with a red carpet"></div></div>
    <div class="info"><h3>Famous Voices<br>in Print</h3><div class="author">Arthur: Warren Vessel</div><div class="price">Price: $ 22</div>
      <div class="stars"><svg><use href="#star"/></svg><svg><use href="#star"/></svg><svg><use href="#star"/></svg><svg><use href="#star"/></svg><svg><use href="#star"/></svg></div>
      <div class="btn-view">View Book</div><div class="btn-cart">Add to Cart</div></div>
  </article>
  <article class="book">
    <div class="thumb"><div class="art-dusk" role="img" aria-label="Dark book cover with a portrait"></div></div>
    <div class="info"><h3>Dusk Chronicle<br>(Umbra)</h3><div class="author">Arthur: Stella Marlow</div><div class="price">Price: $ 30</div>
      <div class="stars"><svg><use href="#star"/></svg><svg><use href="#star"/></svg><svg><use href="#star"/></svg><svg><use href="#star"/></svg></div>
      <div class="btn-view">View Book</div><div class="btn-cart">Add to Cart</div></div>
  </article>
</section>

<section class="abs promo">
  <div class="abs promo-art" role="img" aria-label="Stack of book covers"></div>
  <div class="abs promo-line1">BOOKS <span>AVAILABLE</span> <em>in</em></div>
  <div class="abs promo-rule"></div>
  <div class="abs promo-line2">DISCOUNTED <span>PRICE</span></div>
</section>
<div class="abs divider"></div>
<div class="abs news-title">Newsletter</div>
<div class="abs news-input">Enter Email Address</div>
<div class="abs news-btn">SIGNUP NOW!</div>

<footer class="abs footer">
  <nav><span>HOME</span><span class="sep">|</span><span>ABOUT US</span><span class="sep">|</span><span>SERVICES</span><span class="sep">|</span><span>ALL BOOKS</span><span class="sep">|</span><span>CONTACT US</span></nav>
  <span class="copy">COPYRIGHT © 2013 LEAFMARK. ALL RIGHTS RESERVED.</span>
</footer>
</body>
</html>
```